Looking for business card/letterhead/email signature

Take existing logo and create full design suite of collateral

Contact Information for Business Card

Use mock details that can be edited by us

Font styles to use
Sans Serif

```html
<!DOCTYPE html>
<html lang="en">
<head>
<meta charset="utf-8">
<title>Harlow Digital – Stationery Suite</title>
<link href="https://fonts.googleapis.com/css2?family=Poppins:wght@400;500;700&display=swap" rel="stylesheet">
<style>
  :root {
    --bg: #e4e7e6;
    --paper: #ffffff;
    --card-grey: #f4f5f5;
    --navy: #0d3f8f;
    --navy-faint: #d3deee;
    --accent: #e61d7c;
    --ink: #2b2b2b;
    --shadow: 0 6px 14px rgba(0,0,0,0.12);
  }
  * { box-sizing: border-box; margin: 0; padding: 0; }
  html, body { width: 1200px; height: 900px; overflow: hidden; }
  body {
    background: var(--bg);
    font-family: "Poppins", sans-serif;
    position: relative;
  }
  .sheet {
    position: absolute;
    background: var(--paper);
    box-shadow: var(--shadow);
  }
  .brand {
    display: inline-flex;
    align-items: center;
    gap: 0.35em;
    color: var(--navy);
    font-weight: 700;
    letter-spacing: -0.01em;
    white-space: nowrap;
    line-height: 1;
  }
  .brand-dot {
    width: 0.45em; height: 0.45em;
    border-radius: 50%;
    background: var(--accent);
    flex: none;
  }
  /* letterhead */
  .letterhead { left: 330px; top: 40px; width: 320px; height: 452px; }
  .letterhead .brand { position: absolute; left: 26px; top: 26px; font-size: 17px; }
  /* cover sheet */
  .cover { left: 700px; top: 200px; width: 460px; height: 650px; }
  .cover .brand {
    position: absolute; left: 50%; top: 50%;
    transform: translate(-50%, -50%);
    font-size: 44px;
  }
  /* compliments slip */
  .slip { left: 290px; top: 540px; width: 380px; height: 220px; }
  .slip .brand { position: absolute; left: 24px; top: 24px; font-size: 15px; }
  /* business cards */
  .card { left: 30px; width: 220px; height: 136px; }
  .card-back { top: 330px; background: var(--paper); overflow: hidden; }
  .card-back .brand { position: absolute; left: 12px; top: 12px; font-size: 12px; }
  .card-back .brand-ghost {
    position: absolute; left: 12px; top: 32px;
    font-size: 20px; font-weight: 700; line-height: 1;
    color: var(--navy-faint);
    white-space: nowrap;
  }
  .contact {
    position: absolute; left: 12px; right: 12px; bottom: 10px;
    display: flex; justify-content: space-between; align-items: flex-end;
    color: var(--ink);
  }
  .contact-person { font-size: 8px; line-height: 1.4; }
  .contact .name { font-size: 10px; font-weight: 700; }
  .contact .role { border-top: 1px solid var(--ink); padding-top: 2px; margin-top: 2px; display: inline-block; }
  .contact-details { text-align: right; font-size: 7px; line-height: 1.45; }
  .card-front {
    top: 498px; background: var(--card-grey);
    display: flex; align-items: center; justify-content: center;
  }
  .card-front .brand { font-size: 18px; }
</style>
</head>
<body>

  <section class="sheet letterhead" aria-label="Letterhead">
    <div class="brand"><span>Harlow Digital</span><span class="brand-dot"></span></div>
  </section>

  <section class="sheet cover" aria-label="Cover sheet">
    <div class="brand"><span>Harlow Digital</span><span class="brand-dot"></span></div>
  </section>

  <section class="sheet slip" aria-label="Compliments slip">
    <div class="brand"><span>Harlow Digital</span><span class="brand-dot"></span></div>
  </section>

  <section class="sheet card card-back" aria-label="Business card, contact side">
    <div class="brand"><span>Harlow Digital</span><span class="brand-dot"></span></div>
    <div class="brand-ghost" aria-hidden="true">Harlow Digital</div>
    <div class="contact">
      <div class="contact-person">
        <div class="name">Jhon Doe</div>
        <div class="role">Founder</div>
      </div>
      <div class="contact-details">
        <div>xx building xx floor</div>
        <div>xx.xx city state nation</div>
        <div>Phone: +xx-xxx-xxxx</div>
        <div>Fax: +xx-xxx-xxxx</div>
        <div>E-Mail: xxxx@xxxxxx.xxx</div>
      </div>
    </div>
  </section>

  <section class="sheet card card-front" aria-label="Business card, brand side">
    <div class="brand"><span>Harlow Digital</span><span class="brand-dot"></span></div>
  </section>

</body>
</html>
```